Computer consultant business card

Brimlo Software is a newly started computer consulting company. It's a small one-man company that provides mostly Velunix applications but also websites in collaboration with designers. I'm running this company on the side of full time university studies.

I want the final design to be clean and memorable. Be creative! :)

Some inspiration:
http://www.tavelpix.net/design/73519
http://www.tavelpix.net/design/2739566/business-card-design-by-quillbop
http://www.tavelpix.net/design/804613/business-card-design-by-lorvena-brukwaldsen

See attachment for my company logo.
Updates

I would like to thank everyone for submitting! I'll need a couple of days to review and ultimately select a design.

Target Market(s)

Non-technical entrepreneurs and small companies.

Industry/Entity Type

University

Requirements
Must have
• My company logo.
In any way, both colors from my logo.
First- and last name, e-mail and phone number.
Double-sided design.
Nice to have
• Something creative with the symbol in my logo

```html
<!DOCTYPE html>
<html lang="en">
<head>
<meta charset="utf-8">
<title>Brimlo Software – Business Card</title>
<link rel="stylesheet" href="https://fonts.googleapis.com/css2?family=Questrial&family=EB+Garamond&display=swap">
<style>
  :root {
    --cyan: #86e3f7;
    --ink: #222628;
    --front-light: #d3dadb;
    --front-dark: #a9b8b8;
    --back-outer: #a9b6b5;
    --back-panel: #92a5a3;
    --faint-mark: #879a99;
    --divider: #e6ecec;
    --white: #ffffff;
  }
  * { margin: 0; padding: 0; box-sizing: border-box; }
  html, body { width: 1200px; height: 1038px; overflow: hidden; background: var(--divider); }
  .canvas { position: relative; width: 1200px; height: 1038px; }

  .card { position: absolute; top: 0; height: 1038px; overflow: hidden; }
  .card--front {
    left: 0; width: 598px;
    background: radial-gradient(circle at 50% 49%, var(--front-light) 0%, var(--front-dark) 70%);
  }
  .card--back { left: 602px; width: 598px; background: var(--back-outer); }

  .band { position: absolute; height: 27px; background: var(--cyan); }
  .band--top { top: 0; }
  .band--bottom { bottom: 0; }
  .card--front .band { left: 21px; width: 554px; }
  .card--back .band { left: 22px; width: 554px; }

  .back-panel {
    position: absolute; left: 22px; top: 29px; width: 554px; height: 979px;
    background: var(--back-panel);
  }

  .brand {
    position: absolute; display: flex; align-items: center;
    font-family: "Questrial", sans-serif; color: var(--ink);
  }
  .brand__dot { border-radius: 50%; background: var(--cyan); flex: none; }
  .brand--front { left: 0; width: 598px; top: 440px; justify-content: center; gap: 26px; }
  .brand--front .brand__dot { width: 110px; height: 110px; }
  .brand--front .brand__name { font-size: 96px; line-height: 1; }

  .brand--back { left: 86px; top: 84px; gap: 32px; }
  .brand--back .brand__dot { width: 118px; height: 118px; }
  .brand--back .brand__name { font-size: 88px; line-height: 1; }

  .faint-mark {
    position: absolute; left: 86px; top: 286px; width: 426px; height: 426px;
    border-radius: 50%; background: var(--faint-mark);
  }

  .contact { position: absolute; left: 22px; width: 554px; text-align: center; }
  .contact__name {
    top: 804px; font-family: "Questrial", sans-serif; font-size: 60px; line-height: 1;
    color: var(--cyan); letter-spacing: 1px; word-spacing: 12px;
  }
  .contact__line {
    font-family: "EB Garamond", serif; font-size: 29px; color: var(--white); line-height: 1;
  }
  .contact__phone { top: 928px; }
  .contact__email { top: 968px; }
</style>
</head>
<body>
<main class="canvas">
  <section class="card card--front" aria-label="Card front">
    <div class="band band--top"></div>
    <div class="brand brand--front">
      <span class="brand__dot"></span>
      <span class="brand__name">brimlo</span>
    </div>
    <div class="band band--bottom"></div>
  </section>

  <section class="card card--back" aria-label="Card back">
    <div class="band band--top"></div>
    <div class="back-panel"></div>
    <div class="brand brand--back">
      <span class="brand__dot"></span>
      <span class="brand__name">brimlo</span>
    </div>
    <div class="faint-mark"></div>
    <p class="contact contact__name">Your Name</p>
    <p class="contact contact__line contact__phone">+1555019283746</p>
    <p class="contact contact__line contact__email">yourname@postvel.com</p>
    <div class="band band--bottom"></div>
  </section>
</main>
</body>
</html>
```